International Railway Company Needs a Brochure - KVO Steady & Exact for Railway

We need a brochure for an International Company based in Italy called 'KVO'. We develop innovative instruments used in Railway monitoring for diagnostic and maintenance. Our main product is Rail Contour Scanning Unit (RCSU) - RCSU measuring the track geometry is composed by two profile measurement instruments (left and right) and one inertial pack. All these instruments are installed on a single rigid rod, mounted on a bogie All our products are based on Laser Triangulation Method.
We appreciate to see designs that use color blue but is not required.
The final design should communicate financial safety and growth. Also The final design should communicate our motto 'Steady & Exact'.
We'll send you our Company Logo, photos and contents. We are open to any suggestions.

Our web site is http://www.kvoexample.it/home.html
Updates

We are launching the contest for KVO new logo. It will be finished in 2/5 days. Thanks for your work.

 

Target Market(s)

Our main customers are International Railway Companies (FLVQ-France, KH-Germany, TPO-Italy, ZWN-Switzerland) but also private companies.

Industry/Entity Type

Financial

Requirements
Must have
• The brochure must have 6 pages A4 format like the example file QFA Rail Gauging Suite_EN_v6

Page 1: Cover Page - KVO Synthesis
Page 2: Synthesis of the following products with one image for each

BNX
RCSU
WLHC
GXPT
HQL
PZ

Page 3: RCSU details
Page 4: BNX and WLHC details
Page 5: GXPT and HQL and PZ details
Page 6: Contacts

The text is not important. We can add it in a second time.

Please feel free to change color at both logo if you need to do it or make it trasparent.
Should not have
• In the final brochure we don't want to see our VAT/TVA/IVA

```html
<!DOCTYPE html>
<html lang="en">
<head>
<meta charset="utf-8">
<title>KVO Brochure Spread</title>
<link href="https://fonts.googleapis.com/css2?family=Roboto:wght@300;400;700;900&family=Roboto+Mono:wght@400&display=swap" rel="stylesheet">
<style>
  :root{
    --bg:#e6e6e6;
    --page:#ffffff;
    --ink:#1e1e1e;
    --black:#0e0e0e;
    --orange:#d9531e;
    --orange-deep:#cf4d1b;
    --rule:#2a2a2a;
    --plot:#c9c59c;
    --plot-line:#2f5d93;
  }
  *{box-sizing:border-box;margin:0;padding:0}
  html,body{width:1200px;height:1000px;overflow:hidden;background:var(--bg);font-family:"Roboto",Arial,sans-serif;color:var(--ink)}
  .canvas{position:relative;width:1200px;height:1000px}
  .page{position:absolute;top:123px;width:507px;height:717px;background:var(--page);overflow:hidden}
  .page--left{left:88px;background:linear-gradient(90deg,#fff 62%,#e6e6e6 100%)}
  .page--right{left:595px;background:linear-gradient(90deg,#dcdcdc 0%,#fff 9%)}
  .abs{position:absolute}

  /* left page */
  .rail-photo{left:0;top:0;width:230px;height:717px}
  .intro-box{left:0;top:29px;width:469px;height:123px;background:var(--black)}
  .intro-text{left:98px;top:44px;width:368px;color:#fff;font-size:8.4px;font-weight:700;line-height:11.3px;text-align:justify}
  .brand{display:flex;align-items:center;gap:5px;color:var(--orange);font-weight:700;font-size:15px;letter-spacing:1px}
  .brand-mark{width:10px;height:10px;background:var(--orange)}
  .brand--intro{left:30px;top:76px}
  .tagline{left:24px;top:98px;color:var(--orange);font-size:5.5px;letter-spacing:1px;text-transform:uppercase}
  .brand-tile{left:0;top:177px;width:87px;height:52px;background:var(--black);display:flex;align-items:center;justify-content:center}
  .brand-tile .brand{color:#fff;font-size:14px}
  .brand-tile .brand-mark{background:#fff}
  .product-title{color:var(--orange);font-weight:700;font-size:15px;line-height:18px}
  .product-text{font-size:11.3px;line-height:14px;color:#222}
  .product-text span{display:block;white-space:nowrap}
  .thumb{left:350px;width:118px}
  .bracket{left:469px;top:92px;width:38px;height:400px}
  .slogan{left:240px;top:628px;color:var(--orange)}
  .slogan-main{font-size:21px;font-weight:700;letter-spacing:.3px;line-height:24px}
  .slogan-sub{font-size:15.5px;font-weight:300;letter-spacing:.6px;line-height:18px}
  .footer-band{left:0;top:685px;width:212px;height:32px;background:var(--black)}
  .footer-band .brand{position:absolute;left:18px;top:8px;color:#fff;font-size:15px}
  .footer-band .brand-mark{background:#fff}
  .brand--foot{left:18px;top:656px;color:#fff}
  .brand--foot .brand-mark{background:#fff}
  .rule-left{left:212px;top:701px;width:270px;height:1.5px;background:var(--rule)}

  /* right page */
  .section-tab{left:1px;top:29px;width:115px;height:48px;background:var(--black);color:var(--orange);font-weight:700;font-size:23px;display:flex;align-items:center;justify-content:center;letter-spacing:.5px}
  .hero-photo{left:1px;top:82px;width:409px;height:155px}
  .filler{left:17px;top:253px;width:236px;font-family:"Roboto Mono",monospace;font-size:8.6px;line-height:14.8px;color:#333;letter-spacing:-.6px}
  .filler span{display:block;white-space:nowrap}
  .screen{left:258px;top:255px;width:225px;height:264px}
  .accent-box{left:335px;top:535px;width:172px;height:134px;background:var(--orange-deep);padding:14px 0 0 32px;color:#fff;font-size:11.5px;line-height:16.5px;letter-spacing:.2px}
  .track-frame{left:1px;top:535px;width:350px;height:134px}
  .rule-right{left:5px;top:701px;width:340px;height:1.5px;background:var(--rule)}
  .web{right:14px;top:693px;font-size:13.5px;font-style:italic;color:#222}
  .web b{font-weight:700}
  .screen-text{font-family:"Roboto",Arial,sans-serif}
</style>
</head>
<body>
<div class="canvas">

  <!-- LEFT PAGE -->
  <section class="page page--left">
    <svg class="abs rail-photo" viewBox="0 0 230 717" role="img" aria-label="Black and white photo of a railway track seen from above, running down the page">
      <defs>
        <linearGradient id="railGrad" x1="0" y1="0" x2="1" y2="0">
          <stop offset="0" stop-color="#3c3c3c"/>
          <stop offset=".45" stop-color="#5a5a5a"/>
          <stop offset=".75" stop-color="#2e2e2e"/>
          <stop offset="1" stop-color="#6e6e6e"/>
        </linearGradient>
      </defs>
      <path d="M0 0 H62 Q70 30 70 60 L222 717 H0 Z" fill="url(#railGrad)"/>
    </svg>

    <div class="abs intro-box"></div>
    <div class="abs brand brand--intro"><span class="brand-mark"></span>KVO</div>
    <div class="abs tagline">Steady &amp; Exact</div>
    <p class="abs intro-text">KVO has probably the longest and more sound experience in the world in measuring the rail profile with an accuracy good enough to evaluate the wheel-rail interface dynamics, including the equivalent conicity. The equivalent conicity will soon be a mandatory parameter to control for every main line. The interoperability of different train types, especially on high speed lines, demands for a tight control of the track parameters. The track parameters must meet the UIC518 and UIC519 values, as the trains have been certified according to track conditions assessed in these leaflets. KVO has pioneered this work: the KVO software has been used by the UIC519 commission to check the algorithms in the norm.</p>

    <div class="abs brand-tile"><div class="brand"><span class="brand-mark"></span>KVO</div></div>

    <h2 class="abs product-title" style="left:105px;top:187px">BNX</h2>
    <p class="abs product-text" style="left:108px;top:205px">
      <span>The system not only automates the legacy</span>
      <span style="margin-left:4px">turnouts inspection, but adds much more:</span>
      <span style="margin-left:8px">Complete 3D geometry</span>
      <span style="margin-left:11px">A cross section every 20 mm</span>
      <span style="margin-left:16px">Measurements under load</span>
      <span style="margin-left:19px">Visual inspection.</span>
    </p>
    <svg class="abs thumb" style="top:199px;height:90px" viewBox="0 0 118 90" role="img" aria-label="3D rendering of the BNX measuring unit">
      <defs>
        <linearGradient id="bnxGrad" x1="0" y1="0" x2="1" y2="1">
          <stop offset="0" stop-color="#c7ccc6"/>
          <stop offset="1" stop-color="#7d8a80"/>
        </linearGradient>
      </defs>
      <path d="M14 30 L70 10 L110 36 L110 62 L54 84 L14 60 Z" fill="url(#bnxGrad)"/>
    </svg>

    <h2 class="abs product-title" style="left:145px;top:338px">RCSU</h2>
    <p class="abs product-text" style="left:138px;top:355px;width:205px;text-align:justify;text-align-last:center">
      <span style="text-align:center">Profiles and gauge measurement</span>
      <span style="text-align:center">up to 350 Km/h Wheel/rail contact</span>
      <span style="text-align:center">geometry and equivalent conicity</span>
      <span style="text-align:center">(continuous plot) up to 350 Km/h</span>
      <span style="text-align:center">High accuracy rail profile for</span>
      <span style="text-align:center">application on grinders.</span>
    </p>
    <svg class="abs thumb" style="top:317px;height:93px" viewBox="0 0 118 93" role="img" aria-label="Technical rendering of the RCSU sensors mounted on a bogie">
      <defs>
        <linearGradient id="rcsuGrad" x1="0" y1="0" x2="1" y2="1">
          <stop offset="0" stop-color="#d6d8dc"/>
          <stop offset=".5" stop-color="#8f9aa6"/>
          <stop offset="1" stop-color="#b58a4a"/>
        </linearGradient>
      </defs>
      <rect width="118" height="93" fill="url(#rcsuGrad)"/>
    </svg>

    <h2 class="abs product-title" style="left:188px;top:502px">WLHC</h2>
    <p class="abs product-text" style="left:190px;top:520px">
      <span>The Optical Rail Profile</span>
      <span>Measurement&nbsp;&nbsp;&nbsp;&nbsp;&nbsp;&nbsp;&nbsp;&nbsp;&nbsp;System</span>
      <span>was developed for high</span>
      <span style="margin-left:10px">accuracy measurement of tracks profile. It is also</span>
      <span style="margin-left:10px">used by personnel dealing with high-speed trains,</span>
      <span style="margin-left:14px">sensitive to running dynamics.</span>
    </p>
    <svg class="abs thumb" style="top:449px;height:98px" viewBox="0 0 118 98" role="img" aria-label="Photo of the WLHC instrument fixed under a rail vehicle">
      <defs>
        <linearGradient id="wlhcGrad" x1="0" y1="0" x2="0" y2="1">
          <stop offset="0" stop-color="#9a9a9a"/>
          <stop offset=".6" stop-color="#5e5e5e"/>
          <stop offset="1" stop-color="#4a453f"/>
        </linearGradient>
      </defs>
      <rect width="118" height="98" fill="url(#wlhcGrad)"/>
    </svg>

    <svg class="abs bracket" viewBox="0 0 38 400" aria-hidden="true">
      <path d="M0 1 H12 V395 H0 M0 278 H12 M12 145 H38" fill="none" stroke="#444" stroke-width="1"/>
    </svg>

    <div class="abs slogan">
      <div class="slogan-main">ALWAYS AT THE EDGE</div>
      <div class="slogan-sub">OF THE TECHNOLOGY</div>
    </div>

    <div class="abs brand brand--foot"><span class="brand-mark"></span>KVO</div>
    <div class="abs footer-band"><div class="brand"><span class="brand-mark"></span>KVO</div></div>
    <div class="abs rule-left"></div>
  </section>

  <!-- RIGHT PAGE -->
  <section class="page page--right">
    <div class="abs section-tab">RCSU</div>
    <svg class="abs hero-photo" viewBox="0 0 409 155" preserveAspectRatio="none" role="img" aria-label="Photo of the RCSU measuring beam with red mounts installed under a train">
      <defs>
        <linearGradient id="heroGrad" x1="0" y1="0" x2="0" y2="1">
          <stop offset="0" stop-color="#6b3a36"/>
          <stop offset=".3" stop-color="#2a2a2a"/>
          <stop offset=".7" stop-color="#1c1c1c"/>
          <stop offset="1" stop-color="#6a6660"/>
        </linearGradient>
      </defs>
      <path d="M0 0 H369 A40 40 0 0 1 409 40 V115 A40 40 0 0 1 369 155 H0 Z" fill="#d8d8d8"/>
      <path d="M0 0 H362 A37 37 0 0 1 399 37 V118 A37 37 0 0 1 362 155 H0 Z" fill="url(#heroGrad)"/>
    </svg>

    <p class="abs filler">
      <span>xxxxxxxxxxxxxxxxxxxxxxxxxxxxxxxxxxxxxxxxxxxx</span>
      <span>xxxxxxxxxxxxxxxxxxxxxxxxxxxxxxxxxxxxxxxxxxxx</span>
      <span>xxxxxxxxxxxxxxxxxxxxxxxxxxxxxxxxxxxxxxxxxxxx</span>
      <span>xxxxxxxxxxxxxxxxxxxxxxxxxxxxxxxxxxxxxxxxxxxx</span>
      <span>xxxxxxxxxxxxxxxxxxxxxxxxxxxxxxxxxxxxxxxxxxxx</span>
      <span>xxxxxxxxxxxxxxxxxxxxxxxxxxxxxxxxxxxxxxxxxxxx</span>
      <span>xx xxxxxxxxxxxxxxxxxxxxxxxxxxxxxxxxxxxxxxxxx</span>
      <span>xxxxxxxxxxxxxxxxxxxxxxxxxxxxxxxxxxxxxxxxxxxx</span>
      <span>xxxxxxxxxxxxxxxxxxxxxxxxxxxxxxxxxxxxxxxxxxxx</span>
      <span>xxxxxxxxxxxxxxxxxxxxxxxxxxxxxxxxxxxxxxxxxxxx</span>
      <span>xx xxxxxxxxxxxxxxxxxxxxxxxxxxxxxxxxxxxxxxxxx</span>
      <span>xxxxxxxxxxxxxxxxxxxxxxxxxxxxxxxxxxxxxxxxxxxx</span>
      <span>xxxxxxxxxxxxxxxxxxxxxxxxxxxxxxxxxxxxxxxxxxxx</span>
      <span>xxxxxxxxxxxxxxxxxxxxxxxxxxxxxxxxxxxxxxxxxxxx</span>
      <span>xxxxxxxxxxxxxxxxxxxxxxxxxxxxxxxxxxxxxxxxxxxx</span>
      <span>xxxxxxxxxxxxxxxxxxxxxxxxxxxxxxxxxxxxxxxxxxxx</span>
      <span>xx xxxxxxxxxxxxxxxxxxxxxxxxxxxxxxxxxxxxxxxxx</span>
    </p>

    <svg class="abs screen screen-text" viewBox="0 0 225 264" aria-label="Software linear view of a turnout with curvature, gauge and alignment line plots">
      <rect width="225" height="264" fill="#f4f4f4" stroke="#c4c4c4"/>
      <rect width="225" height="12" fill="#dfe4ea"/>
      <text x="3" y="9" font-size="5.5" font-weight="700" fill="#2d4c74">Linear View - Turnout ID: 17</text>
      <rect y="13" width="225" height="8" fill="#f1d9a6"/>
      <g font-size="6.5" fill="#222">
        <text x="2" y="34">35m</text><text x="27" y="34">30m</text><text x="52" y="34">25m</text>
        <text x="79" y="34">20m</text><text x="106" y="34">15m</text><text x="132" y="34">10m</text>
        <text x="159" y="34">5m</text><text x="185" y="34">0m</text><text x="210" y="34">-5m</text>
      </g>
      <g stroke="#555" stroke-width=".6">
        <path d="M9 38 v4 M34 38 v4 M59 38 v4 M86 38 v4 M112 38 v4 M138 38 v4 M163 38 v4 M189 38 v4 M215 38 v4"/>
      </g>
      <rect x="2" y="48" width="221" height="58" fill="#2b2b2b"/>
      <path d="M2 70 H223 M2 86 H223" stroke="#8a8a8a" stroke-width="1"/>
      <path d="M60 86 Q130 80 200 70" stroke="#9a9a9a" stroke-width="1" fill="none"/>
      <text x="3" y="116" font-size="5" font-weight="700" fill="#2d4c74">Curvatura</text>
      <path d="M2 120 Q110 112 223 120" stroke="var(--plot-line)" stroke-width="1" fill="none"/>
      <text x="3" y="137" font-size="5" font-weight="700" fill="#2d4c74">Scartamento</text>
      <text x="3" y="144" font-size="5" fill="#2d4c74">1442.02</text>
      <rect x="2" y="150" width="221" height="48" fill="var(--plot)"/>
      <path d="M2 186 L40 186 L50 178 L60 186 L110 188 L150 184 L185 186 L188 132 L191 186 L223 186" stroke="var(--plot-line)" stroke-width="1" fill="none"/>
      <path d="M188 132 V186" stroke="#c0282a" stroke-width="1"/>
      <path d="M132 112 V260" stroke="#555" stroke-width=".5"/>
      <text x="3" y="214" font-size="5" font-weight="700" fill="#2d4c74">Allineamento</text>
      <rect x="2" y="220" width="221" height="38" fill="var(--plot)"/>
      <path d="M2 238 Q40 232 80 240 T160 236 T223 240" stroke="var(--plot-line)" stroke-width="1" fill="none"/>
    </svg>

    <div class="abs accent-box">xxxxxxxxxxxxxxxx<br>xxxxxxxxxxxxxxxx<br>xxxxxxxxxxxxxxxx<br>xxxxxxxxxxxxxxxx<br>xxxxxxxxxxxxxxxx</div>
    <svg class="abs track-frame" viewBox="0 0 350 134" preserveAspectRatio="none" role="img" aria-label="Photo of railway tracks converging at a station under an overcast sky">
      <defs>
        <linearGradient id="trackGrad" x1="0" y1="0" x2="0" y2="1">
          <stop offset="0" stop-color="#6e7480"/>
          <stop offset=".4" stop-color="#4a4540"/>
          <stop offset="1" stop-color="#6b5f55"/>
        </linearGradient>
      </defs>
      <path d="M0 0 H320 A30 30 0 0 1 350 30 V104 A30 30 0 0 1 320 134 H0 Z" fill="#d8d8d8"/>
      <path d="M0 0 H316 A28 28 0 0 1 344 28 V106 A28 28 0 0 1 316 134 H0 Z" fill="url(#trackGrad)"/>
    </svg>
    <div class="abs brand" style="left:26px;top:591px;color:#fff"><span class="brand-mark" style="background:#fff"></span>KVO</div>

    <div class="abs rule-right"></div>
    <div class="abs web">www.<b>kvo</b>example.it</div>
  </section>

</div>
</body>
</html>
```